Business cards / Letterheads / Compliment slips

We are looking to get business cards, letterheads and compliment slips designed.

These will all have to follow the design of our new website and logo. Links to the website, logo and fonts can be found below...

The designs need to be simple with focus on the typography. Only the following colours should be used on the designs...

#7f9d3c
#191818
#fff

Website:
http://brookfieldweb.examplestudio.co.uk/

Logo:
https://www.filecrate.example/sh/8kd2m4qwzpla7ve/hTr5NpQ2Xw/logos

Fonts:
https://www.filecrate.example/sh/8kd2m4qwzpla7ve/Q9vTzR3mKe/Fonts/BayerModern_TTF

and

https://www.filecrate.example/sh/8kd2m4qwzpla7ve/W7nHcY5pD3/Fonts/MuseoSansFamily

Reason: We would like some more design submissions

Reason: We are still deciding on designs we like and would like to see some more submissions...

Industry/Entity Type

Business

Requirements
Must have
• The designs need to be simple with focus on the typography. Only the following colours should be used on the designs...

#7f9d3c
#191818
#fff
Should not have
• - Any fonts that are not provided.
- Any colours that are not provided.

```html
<!DOCTYPE html>
<html lang="en">
<head>
<meta charset="utf-8">
<title>brookfieldweb stationery</title>
<link rel="stylesheet" href="https://fonts.googleapis.com/css2?family=Varela+Round&family=Dancing+Script:wght@500&display=swap">
<style>
  :root {
    --green: #7f9d3c;
    --ink: #191818;
    --band: #3e3f3d;
    --paper: #ffffff;
    --backdrop: #e4e4e2;
    --muted: #8a8a88;
    --sans: "Varela Round", sans-serif;
    --script: "Dancing Script", cursive;
  }
  * { box-sizing: border-box; margin: 0; padding: 0; }
  html, body { width: 1200px; height: 800px; overflow: hidden; }
  body { background: var(--backdrop); font-family: var(--sans); color: var(--ink); position: relative; }

  .sheet { position: absolute; background: var(--paper); box-shadow: 0 2px 10px rgba(0,0,0,.12); }

  .letterhead { left: 60px; top: 40px; width: 500px; height: 707px; }
  .compliment-slip { left: 600px; top: 40px; width: 540px; height: 255px; }
  .card-front { left: 600px; top: 335px; width: 260px; height: 168px; }
  .card-back { left: 880px; top: 335px; width: 260px; height: 168px; background: var(--band); overflow: hidden; }

  .header-band {
    position: absolute; left: 18px; right: 18px; top: 20px; height: 46px;
    background: var(--band); border-radius: 10px;
    display: flex; align-items: center; justify-content: space-between; padding: 0 16px;
  }
  .brand { display: flex; align-items: center; gap: 7px; font-size: 19px; color: var(--paper); letter-spacing: -.2px; white-space: nowrap; }
  .brand-dot { width: 16px; height: 16px; border-radius: 50%; background: var(--green); flex: none; }
  .brand.on-light { color: var(--ink); }

  .contact { list-style: none; font-size: 6.5px; line-height: 9px; text-align: right; color: var(--paper); white-space: nowrap; }
  .contact li::after { content: ""; display: inline-block; width: 4px; height: 4px; border-radius: 50%; background: var(--green); margin-left: 4px; vertical-align: middle; }
  .contact.on-light { color: var(--ink); }

  .greeting { position: absolute; left: 40px; bottom: 32px; font-family: var(--script); font-size: 34px; color: var(--band); }

  .card-front .brand { position: absolute; left: 18px; top: 100px; font-size: 17px; }
  .card-front .brand-dot { width: 14px; height: 14px; }
  .holder { position: absolute; right: 18px; top: 28px; text-align: right; }
  .holder-name { font-size: 12px; color: var(--ink); white-space: nowrap; }
  .holder-role { font-size: 6px; color: var(--muted); margin-top: 1px; }
  .card-front .contact { position: absolute; right: 18px; top: 58px; }

  .back-mark { position: absolute; left: 72px; top: 26px; width: 116px; height: 116px; border-radius: 50%; background: var(--green); }

  .lockup { position: absolute; left: 600px; top: 560px; display: flex; align-items: center; gap: 14px; font-size: 56px; color: var(--ink); letter-spacing: -1px; white-space: nowrap; }
  .lockup .brand-dot { width: 46px; height: 46px; }
</style>
</head>
<body>

  <section class="sheet letterhead" aria-label="Letterhead">
    <header class="header-band">
      <div class="brand"><span class="brand-dot"></span>brookfieldweb</div>
      <ul class="contact">
        <li>PO Box 12, Townsville</li>
        <li>+44 123 456 7890</li>
        <li>info@brookfieldweb.co.uk</li>
        <li>www.brookfieldweb.co.uk</li>
      </ul>
    </header>
  </section>

  <section class="sheet compliment-slip" aria-label="Compliment slip">
    <header class="header-band">
      <div class="brand"><span class="brand-dot"></span>brookfieldweb</div>
      <ul class="contact">
        <li>PO Box 12, Townsville</li>
        <li>+44 123 456 7890</li>
        <li>info@brookfieldweb.co.uk</li>
        <li>www.brookfieldweb.co.uk</li>
      </ul>
    </header>
    <p class="greeting">With Compliments</p>
  </section>

  <section class="sheet card-front" aria-label="Business card front">
    <div class="holder">
      <p class="holder-name">Tamsin Ferrow</p>
      <p class="holder-role">Account Manager</p>
    </div>
    <ul class="contact on-light">
      <li>PO Box 12, Townsville</li>
      <li>+44 123 456 7890</li>
      <li>info@brookfieldweb.co.uk</li>
      <li>www.brookfieldweb.co.uk</li>
    </ul>
    <div class="brand on-light"><span class="brand-dot"></span>brookfieldweb</div>
  </section>

  <section class="sheet card-back" aria-label="Business card back">
    <div class="back-mark"></div>
  </section>

  <div class="lockup"><span class="brand-dot"></span>brookfieldweb</div>

</body>
</html>
```